Brisk Lantern Accounting - New client package

I need a stationary package (presentation folder cover, welcome letter template/design, sample financial report template/design, business card and new logo) for my accounting business. I would like to see designs that use the color blue. Financial icons can be included in the design. The final design should be clean and communicate professionalism and the use of modern; user-friendly technology. Attached postcard files should help with overall design concept.

```html
<!DOCTYPE html>
<html lang="en">
<head>
<meta charset="utf-8">
<title>Brisk Lantern Accounting – Business Card</title>
<link href="https://fonts.googleapis.com/css2?family=Roboto:wght@400;500&family=Saira+Condensed:wght@500&display=swap" rel="stylesheet">
<style>
  :root {
    --backdrop: #181818;
    --card: #f8f8f8;
    --brand-blue: #2d5b8b;
    --charcoal: #3c4144;
    --ink: #3a3a3a;
    --white: #ffffff;
  }
  * { margin: 0; padding: 0; box-sizing: border-box; }
  html, body {
    width: 1200px; height: 1200px; overflow: hidden;
    background: var(--backdrop);
    font-family: "Roboto", Arial, sans-serif;
  }
  .card {
    position: absolute;
    left: 318px; width: 562px; height: 339px;
    background: var(--card);
    overflow: hidden;
  }
  .card--front { top: 251px; }
  .card--back { top: 608px; }

  .brand-mark {
    position: absolute;
    border-radius: 50%;
    background: var(--brand-blue);
  }
  .brand-name {
    position: absolute;
    font-family: "Roboto", Arial, sans-serif;
    font-weight: 500;
    color: var(--brand-blue);
    text-transform: uppercase;
    line-height: 1.15;
  }

  /* Front */
  .card--front .brand-mark { left: 226px; top: 65px; width: 112px; height: 112px; }
  .card--front .brand-name {
    left: 0; right: 0; top: 186px; text-align: center;
    font-size: 27px; letter-spacing: 2px;
  }
  .front-web {
    position: absolute; left: 0; right: 0; top: 294px;
    display: flex; justify-content: center; align-items: center; gap: 14px;
    font-size: 14px; color: var(--ink);
  }
  .front-web .dash { width: 38px; height: 3px; background: var(--brand-blue); border-radius: 2px; }
  .front-bar { position: absolute; left: 0; bottom: 0; width: 100%; height: 14px; display: flex; }
  .front-bar span { flex: 1; }
  .front-bar .blue { background: var(--brand-blue); }
  .front-bar .dark { background: var(--charcoal); }

  /* Back */
  .card--back .brand-mark { left: 88px; top: 48px; width: 124px; height: 124px; }
  .card--back .brand-name {
    left: 30px; width: 240px; top: 178px; text-align: center;
    font-size: 21px; letter-spacing: 1.5px;
  }
  .holder {
    position: absolute; right: 28px; top: 42px; text-align: right;
    color: var(--ink);
  }
  .holder-name {
    font-family: "Saira Condensed", "Arial Narrow", sans-serif;
    font-weight: 500; font-size: 24px; color: var(--brand-blue); line-height: 1.1;
  }
  .holder-title { font-size: 14px; margin-top: 4px; }
  .holder-address { font-size: 14px; line-height: 21px; margin-top: 14px; }
  .wave { position: absolute; left: 0; top: 0; }
  .contact {
    position: absolute; right: 22px; top: 258px;
    list-style: none; text-align: right;
    font-size: 14px; line-height: 21px; color: var(--white);
  }
  .contact li { display: flex; justify-content: flex-end; align-items: center; gap: 7px; }
  .contact svg { width: 12px; height: 12px; }
</style>
</head>
<body>

<section class="card card--front">
  <div class="brand-mark"></div>
  <div class="brand-name">Brisk Lantern<br>Accounting</div>
  <div class="front-web"><span class="dash"></span>www.brisklanternaccounting.com<span class="dash"></span></div>
  <div class="front-bar"><span class="blue"></span><span class="dark"></span></div>
</section>

<section class="card card--back">
  <div class="brand-mark"></div>
  <div class="brand-name">Brisk Lantern<br>Accounting</div>

  <div class="holder">
    <div class="holder-name">Nora Ellison</div>
    <div class="holder-title">Managing Director</div>
    <div class="holder-address">58 Harbor Lane,<br>Fairview, US 10234</div>
  </div>

  <svg class="wave" width="562" height="339" viewBox="0 0 562 339" aria-hidden="true">
    <path fill="var(--charcoal)" d="M0,250 C70,300 170,316 260,280 C360,238 450,174 562,174 L562,188 C450,190 360,252 260,292 C170,328 70,322 0,284 Z"/>
    <path fill="var(--brand-blue)" d="M0,296 C70,328 170,338 260,304 C360,264 450,204 562,200 L562,339 L0,339 Z"/>
  </svg>

  <ul class="contact">
    <li>1.800.555.0142
      <svg viewBox="0 0 12 12"><path fill="#fff" d="M1,4 C1,2 3,1.5 6,1.5 C9,1.5 11,2 11,4 L9,5 L8,3.8 L4,3.8 L3,5 Z M3,6 L9,6 L10.5,10.5 L1.5,10.5 Z"/></svg>
    </li>
    <li>www.brisklanternaccounting.com
      <svg viewBox="0 0 12 12"><rect x="0.5" y="2" width="11" height="8" fill="#fff"/><path d="M0.8,2.5 L6,6.8 L11.2,2.5 M0.8,9.5 L4.5,5.6 M11.2,9.5 L7.5,5.6" stroke="var(--brand-blue)" stroke-width="1" fill="none"/></svg>
    </li>
    <li>info@brisklanternaccounting.com
      <svg viewBox="0 0 12 12"><circle cx="6" cy="6" r="5.5" fill="#fff"/><path d="M6,0.5 V11.5 M0.5,6 H11.5 M1.5,3.5 H10.5 M1.5,8.5 H10.5 M6,0.5 C3,3 3,9 6,11.5 M6,0.5 C9,3 9,9 6,11.5" stroke="var(--brand-blue)" stroke-width="0.7" fill="none"/></svg>
    </li>
  </ul>
</section>

</body>
</html>
```